Create a flyer that will catch your eye and make you want to call us for KELVANE seamless Gutters

We are looking for a logo to help us with sales of our seamless gutter business, we are looking to expand, add loyal customers and increase our referral business.
We provide a turn key process from sales to install. we show up with our rolling factory, our truck spits out what seems to be an endless supply of gutter!
Each job is fabricated and installed to meet your homes design.

Target Market(s)

Treasure Coast of Florida, single story Homes

Font styles to use
Serif

Requirements
Must have
• Our Logo and Name on the flyer
Clean design with a clear message
call to action

```html
<!DOCTYPE html>
<html lang="en">
<head>
<meta charset="utf-8">
<title>Kelvane Gutter Works Flyer</title>
<link rel="stylesheet" href="https://fonts.googleapis.com/css2?family=Open+Sans:wght@400;600;700&family=Oswald:wght@500;600&family=Russo+One&display=swap">
<style>
  :root {
    --green: #00a651;
    --green-dark: #008c44;
    --grey: #5f6062;
    --grey-dark: #4a4b4d;
    --text: #333333;
    --paper: #f4f4f4;
    --sky: #3f7fbf;
    --roof: #1f5fa8;
    --wall: #d9d4c3;
    --white: #ffffff;
  }
  * { margin: 0; padding: 0; box-sizing: border-box; }
  html, body { width: 796px; height: 1200px; overflow: hidden; }
  body { font-family: "Open Sans", sans-serif; color: var(--text); }
  .flyer {
    position: relative;
    width: 796px;
    height: 1200px;
    background: radial-gradient(ellipse at 30% 75%, #e2e2e2 0%, var(--paper) 45%, var(--white) 100%);
    overflow: hidden;
  }
  .shapes { position: absolute; inset: 0; }
  .brand {
    position: absolute; left: 52px; top: 40px;
    display: flex; align-items: center; gap: 12px;
  }
  .brand-dot { width: 34px; height: 34px; border-radius: 50%; background: var(--green); }
  .brand-name { font-size: 34px; font-weight: 700; color: var(--green); letter-spacing: -0.5px; }
  .follow {
    position: absolute; right: 60px; top: 52px;
    display: flex; align-items: center; gap: 8px;
    font-size: 22px; font-weight: 700; color: var(--grey-dark);
  }
  .follow-dot { width: 36px; height: 36px; border-radius: 50%; background: var(--green); }
  .follow-label { margin-right: 4px; }
  .content { position: absolute; left: 0; right: 0; top: 560px; text-align: center; }
  .headline {
    font-family: "Russo One", sans-serif; font-size: 64px; line-height: 1;
    color: var(--green); letter-spacing: 0.5px;
  }
  .headline .accent { color: var(--grey-dark); }
  .subhead { margin-top: 10px; font-size: 26px; font-weight: 700; color: var(--grey); }
  .intro { width: 620px; margin: 6px auto 0; font-size: 16px; line-height: 23px; }
  .callout {
    width: 586px; margin: 20px auto 0; padding: 8px 0;
    background: var(--green); color: var(--white);
    font-family: "Oswald", sans-serif; font-weight: 500; font-size: 17px; line-height: 24px;
  }
  .point { font-size: 20px; font-weight: 700; line-height: 28px; color: var(--grey); }
  .point em { font-style: normal; color: var(--green); }
  .point-warranty { margin-top: 24px; }
  .divider { position: relative; width: 536px; height: 1px; margin: 22px auto 20px; background: #9a9a9a; }
  .divider::after {
    content: ""; position: absolute; left: 248px; top: -1px; width: 40px; height: 3px; background: var(--green);
  }
  .cta {
    position: absolute; left: 178px; top: 1032px; width: 408px; height: 92px;
    border-radius: 46px; overflow: hidden; border: 3px solid var(--white);
    font-family: "Oswald", sans-serif; text-align: center;
  }
  .cta-label {
    height: 44px; background: var(--grey-dark); color: var(--white);
    font-size: 22px; font-weight: 600; line-height: 44px;
  }
  .cta-label em { font-style: normal; color: var(--green); }
  .cta-phone {
    height: 48px; background: var(--green); color: var(--white);
    font-size: 40px; font-weight: 600; line-height: 46px;
    display: flex; align-items: center; justify-content: center; gap: 8px;
  }
  .footer {
    position: absolute; left: 0; right: 0; top: 1146px;
    display: flex; justify-content: center; align-items: center; gap: 14px;
    color: var(--white); font-size: 14px; font-weight: 600; line-height: 19px;
  }
  .footer-item { display: flex; align-items: center; gap: 6px; }
  .footer-address { text-align: center; }
  .footer-rule { width: 1px; height: 36px; background: var(--white); }
</style>
</head>
<body>
<main class="flyer">
  <svg class="shapes" width="796" height="1200" viewBox="0 0 796 1200">
    <polygon class="accent-stripe" points="372,211 398,211 450,119 424,119" fill="#00a651"/>
    <polygon class="hero-photo" role="img" aria-label="Photo of a house with a blue tiled roof, white gutters and a brick chimney under a clear blue sky"
      points="0,211 410,211 462,119 796,119 796,549 0,549" fill="url(#heroFill)"/>
    <path class="footer-band" d="M0,1128 Q398,1010 796,1090 L796,1200 L0,1200 Z" fill="#5f6062"/>
    <defs>
      <linearGradient id="heroFill" x1="0" y1="0" x2="0" y2="1">
        <stop offset="0" stop-color="#3f7fbf"/>
        <stop offset="0.45" stop-color="#1f5fa8"/>
        <stop offset="0.6" stop-color="#d9d4c3"/>
        <stop offset="1" stop-color="#b8ae94"/>
      </linearGradient>
    </defs>
  </svg>

  <div class="brand">
    <span class="brand-dot"></span>
    <span class="brand-name">Kelvane Gutter Works</span>
  </div>

  <div class="follow">
    <span class="follow-label">Follow Us</span>
    <span class="follow-dot"></span>
    <span class="follow-dot"></span>
  </div>

  <section class="content">
    <h1 class="headline">Kelvane Gutter <span class="accent">Works</span></h1>
    <h2 class="subhead">Provides Top Quality Seamless Gutter System</h2>
    <p class="intro">That will protect your home for many years. Our traveling Gutter Works on wheels allows us to custom fit gutters to your homes specific need sat a competitive price. We take pride in our excellent customer service, professional installs and quality products.</p>
    <p class="callout">Someone is always available to answer your calls,<br>provide answers to your questions and update you on the progress of your job.</p>
    <p class="point point-warranty">We provide the very best <em>warranty</em> in the business<br>and use the best materials available.</p>
    <div class="divider"></div>
    <p class="point">We provide <em>FREE</em> in home estimates and<br>are adhering to stringent <em>covid-19 protocals.</em></p>
  </section>

  <div class="cta">
    <div class="cta-label">FOR <em>FREE</em> IN HOME ESTIMATES CALL</div>
    <div class="cta-phone">
      <svg width="24" height="24" viewBox="0 0 24 24" aria-hidden="true"><path d="M6.6 10.8a15 15 0 0 0 6.6 6.6l2.2-2.2a1 1 0 0 1 1-.25 11 11 0 0 0 3.6.6 1 1 0 0 1 1 1V20a1 1 0 0 1-1 1A17 17 0 0 1 3 4a1 1 0 0 1 1-1h3.5a1 1 0 0 1 1 1 11 11 0 0 0 .6 3.6 1 1 0 0 1-.25 1z" fill="#ffffff"/></svg>
      <span>555-014-2290</span>
    </div>
  </div>

  <footer class="footer">
    <div class="footer-item">
      <svg width="18" height="18" viewBox="0 0 24 24" aria-hidden="true"><circle cx="12" cy="12" r="11" fill="none" stroke="#fff" stroke-width="1.5"/><path d="M12 5a4.5 4.5 0 0 0-4.5 4.5C7.5 13 12 18.5 12 18.5s4.5-5.5 4.5-9A4.5 4.5 0 0 0 12 5zm0 6.2a1.7 1.7 0 1 1 0-3.4 1.7 1.7 0 0 1 0 3.4z" fill="#fff"/></svg>
      <span class="footer-address">418 N 27<sup>th</sup> Street Harbor Vale,<br>Florida 30418</span>
    </div>
    <span class="footer-rule"></span>
    <div class="footer-item">
      <svg width="18" height="18" viewBox="0 0 24 24" aria-hidden="true"><circle cx="12" cy="12" r="11" fill="none" stroke="#fff" stroke-width="1.5"/><rect x="7" y="9" width="10" height="8" fill="#fff"/><rect x="9" y="6" width="6" height="3" fill="#fff"/></svg>
      <span>Fax 555-014-2291</span>
    </div>
  </footer>
</main>
</body>
</html>
```